Wordpress template for a mens-choire webpage

Task is to design a Wordpress template for an 98 years old estonian mens choire webpage.
Design should involve details from the attached files, choire logo and the colors of the choire flag: in horizontal orientation bright sky-blue, white, bright grass-green.
Designer signature is allowed to be added to the template, with country of origin.

Thank you everyone for your great designs!
Our project has now entered into a voting and decision phase until 14th of March 2014 (included).

```html
<!DOCTYPE html>
<html lang="en">
<head>
<meta charset="utf-8">
<title>Kaljuranna Meeskoor</title>
<link href="https://fonts.googleapis.com/css2?family=Open+Sans:wght@400;600&display=swap" rel="stylesheet">
<style>
:root{
  --sky:#1f6db3;
  --grass:#4f9a1c;
  --grass-light:#6cc02a;
  --white:#ffffff;
  --red:#a8101a;
  --link:#1f6aa8;
  --text:#555555;
  --rule:#d9d9d9;
  --cal-head:#666666;
}
*{box-sizing:border-box;margin:0;padding:0}
html,body{width:1022px;height:1200px;overflow:hidden}
body{position:relative;font-family:"Open Sans",sans-serif;color:var(--text);background:var(--sky)}
.flag-bg{position:absolute;inset:0}
.topbar{position:absolute;top:40px;left:93px;right:93px;display:flex;justify-content:space-between;color:var(--white);font-size:16px}
.panel{position:absolute;left:84px;top:72px;width:854px;height:1030px;background:var(--white);border-radius:3px}
.nav{position:absolute;top:16px;left:0;right:0;height:20px;font-size:13.5px;text-transform:uppercase}
.nav a{position:absolute;color:var(--link);text-decoration:none;white-space:nowrap}
.nav a.active{color:var(--red)}
.crest{position:absolute;left:358px;top:-61px;width:138px;height:138px;border-radius:50%;background:var(--white);border:3px solid #e3c25a;box-shadow:0 2px 6px rgba(0,0,0,.25);display:flex;align-items:center;justify-content:center;text-align:center;color:var(--red);font-size:14px;font-weight:600;line-height:1.2;z-index:2}
.slider{position:absolute;left:9px;top:48px;width:836px;height:319px;border-radius:3px;overflow:hidden;background:linear-gradient(180deg,#b7804f 0%,#5c4634 35%,#1e1d1f 75%,#121214 100%)}
.slider .caption{position:absolute;left:0;right:0;bottom:0;height:48px;background:rgba(20,20,20,.75);color:var(--white);font-size:20px;display:flex;align-items:center;justify-content:center}
.arrow{position:absolute;top:144px;width:28px;height:28px;border-radius:50%;background:rgba(255,255,255,.8)}
.arrow svg{display:block}
h2{font-weight:400;color:var(--red)}
.welcome{position:absolute;left:12px;top:384px;width:830px}
.welcome h2{font-size:21px}
.welcome p{margin-top:9px;font-size:11.6px;line-height:19.5px}
.btn{display:inline-block;margin-top:14px;padding:0 9px;height:26px;line-height:26px;background:#707070;border-radius:3px;color:var(--white);font-size:12px}
.rule{position:absolute;left:10px;width:836px;height:1px;background:var(--rule)}
.services{position:absolute;left:13px;top:582px;width:834px}
.services h2{font-size:17px}
.services .next{position:absolute;right:10px;top:4px;width:14px;height:14px;border-radius:50%;background:#bbb}
.cards{display:flex;gap:17px;margin-top:13px}
.card{width:196px;text-align:center}
.card .photo{height:116px}
.card span{display:block;margin-top:8px;color:var(--link);font-size:13.5px}
.blog{position:absolute;left:13px;top:800px;width:600px}
.blog h2{font-size:17px}
.post{display:flex;gap:17px;margin-top:24px}
.post .photo{width:196px;height:169px;flex:none;background:linear-gradient(180deg,#3b2a22,#5a3a30 60%,#7a5a3a)}
.post h3{font-weight:400;color:var(--red);font-size:13.5px;margin-top:-2px}
.post time{display:block;font-size:11.6px;color:#666;margin-top:3px}
.post p{font-size:11.6px;line-height:18px;margin-top:9px}
.post .more{display:block;color:var(--link);font-size:11.6px;margin-top:7px}
.share{display:flex;gap:6px;margin-top:6px;font-size:10px}
.share span{border:1px solid #ccc;border-radius:2px;padding:1px 4px;color:#444;background:#f6f6f6}
.share .fb{color:#3b5998}
.share .gp{color:#d14836}
.share .sh{background:#e8522f;color:#fff;border-color:#e8522f}
.calendar{position:absolute;left:623px;top:793px;width:217px}
.calendar h2{height:40px;line-height:40px;padding-left:10px;color:var(--white);font-size:17px;background:linear-gradient(180deg,var(--grass-light),var(--grass))}
.cal-grid{display:grid;grid-template-columns:repeat(7,1fr);gap:2px;margin-top:4px;font-size:11.6px;text-align:center}
.cal-grid b{background:var(--cal-head);color:var(--white);font-size:9.5px;font-weight:600;height:22px;line-height:22px}
.cal-grid i{font-style:normal;height:24.7px;line-height:24.7px;border-bottom:1px solid #e5e5e5;color:#333}
.cal-grid i.we{color:#4b3f8f}
.cal-nav{display:flex;justify-content:space-between;align-items:center;margin-top:6px;font-size:9px;color:#888}
.cal-nav strong{font-weight:400;font-size:13px;color:#333}
.footer{position:absolute;left:85px;top:1129px;color:var(--white);font-size:12.5px}
.footer nav a{color:var(--white);text-decoration:none}
.footer nav .sep{margin:0 9px}
.footer p{margin-top:14px;word-spacing:4px}
.social{position:absolute;left:809px;top:1141px;display:flex;gap:13px}
.social span{width:23px;height:23px;border-radius:3px;background:#e6e6e6}
</style>
</head>
<body>
<svg class="flag-bg" width="1022" height="1200" viewBox="0 0 1022 1200" aria-hidden="true">
  <rect width="1022" height="1200" fill="#1f6db3"/>
  <path d="M0 0H1022V300C900 330 700 360 500 380C300 400 150 420 0 436Z" fill="#ffffff"/>
  <path d="M0 0H1022V76C950 90 860 70 760 90C600 110 400 100 250 130C150 150 80 160 0 175Z" fill="#4f9a1c"/>
</svg>

<div class="topbar"><span>CALL US : 555 014 2790</span><span>E-mail : info@kaljurannameeskoor.com</span></div>

<div class="panel">
  <nav class="nav">
    <a class="active" style="left:24px">Home</a>
    <a style="left:111px">About</a>
    <a style="left:186px">Services</a>
    <a style="left:282px">Blog</a>
    <a style="left:525px">Events</a>
    <a style="left:611px">Testimonials</a>
    <a style="left:744px">Contact us</a>
  </nav>
  <div class="crest">Kaljuranna<br>Meeskoor</div>

  <div class="slider" role="img" aria-label="Men's choir in black suits performing on a concert stage">
    <div class="arrow" style="left:14px"><svg width="28" height="28"><path d="M16 9l-5 5 5 5" fill="none" stroke="#999" stroke-width="1.5"/></svg></div>
    <div class="arrow" style="right:14px"><svg width="28" height="28"><path d="M12 9l5 5-5 5" fill="none" stroke="#999" stroke-width="1.5"/></svg></div>
    <div class="caption">98 YEARS OF ESTONIAN CHOIRE</div>
  </div>

  <section class="welcome">
    <h2>Welcome to Kaljuranna Meeskoor</h2>
    <p>Mauris consectetur sed orci in pellentesque. Mauris at placerat sapien, sit amet vehicula metus. Phasellus vitae risus scelerisque, ullamcorper leo eu, aliquam metus. Donec ligula leo, ultrices a felis a, porttitor scelerisque libero. Suspendisse quis sem sit amet metus tincidunt rutrum vitae vitae ligula. Donec aliquet ultrices interdum. Praesent bibendum sed purus nec pharetra. Morbi placerat sagittis commodo. Duis nunc diam, pretium ac blandit eu, lacinia non lectus.</p>
    <span class="btn">Know more</span>
  </section>

  <div class="rule" style="top:557px"></div>

  <section class="services">
    <h2>Our Services</h2>
    <span class="next"></span>
    <div class="cards">
      <div class="card"><div class="photo" role="img" aria-label="Choir singers standing in a line by the sea" style="background:linear-gradient(180deg,#8c9298,#b9bcbf 55%,#7d7a73)"></div><span>COLLEGE CHOIRS</span></div>
      <div class="card"><div class="photo" role="img" aria-label="Choir in blue and violet robes" style="background:linear-gradient(180deg,#ececec 30%,#3a5a8a 60%,#2c4a6c)"></div><span>CHURCH CHOIRS</span></div>
      <div class="card"><div class="photo" role="img" aria-label="Choir in traditional costumes on stone steps" style="background:linear-gradient(180deg,#5f5a52,#2e2a28 55%,#807a70)"></div><span>COMMUNITY CHOIRS</span></div>
      <div class="card"><div class="photo" role="img" aria-label="Male choir in black suits photographed from above" style="background:linear-gradient(180deg,#9c9a96,#3d3b39 50%,#8a8884)"></div><span>MALE CHOIRS</span></div>
    </div>
  </section>

  <div class="rule" style="top:770px"></div>

  <section class="blog">
    <h2>Our Blog</h2>
    <article class="post">
      <div class="photo" role="img" aria-label="Choir in striped blazers performing with a conductor"></div>
      <div>
        <h3>Mauris consectetur sed orci in pellentesque.</h3>
        <time>February 14, 2014</time>
        <p>Mauris at placerat sapien, sit amet vehicula metus. Phasellus vitae risus scelerisque, ullamcorper leo eu, aliquam metus. Donec ligula leo, ultrices a felis a, porttitor scelerisque libero. Suspendisse quis sem sit amet metus tincidunt rutrum vitae vitae ligula.</p>
        <span class="more">KNOW MORE</span>
        <div class="share">
          <span class="fb">Like</span><span>3k</span>
          <span>Tweet</span><span>316</span>
          <span class="gp">+1</span><span>81</span>
          <span class="sh">Share</span><span>4.6K</span>
        </div>
      </div>
    </article>
  </section>

  <aside class="calendar">
    <h2>Our Events Calendar</h2>
    <div class="cal-grid">
      <b>M</b><b>T</b><b>W</b><b>T</b><b>F</b><b>S</b><b>S</b>
      <i></i><i></i><i></i><i>1</i><i>2</i><i class="we">3</i><i class="we">4</i>
      <i>5</i><i>6</i><i>7</i><i>8</i><i>9</i><i class="we">10</i><i class="we">11</i>
      <i>12</i><i>13</i><i>14</i><i>15</i><i>16</i><i class="we">17</i><i class="we">18</i>
      <i>19</i><i>20</i><i>21</i><i>22</i><i>23</i><i class="we">24</i><i class="we">25</i>
      <i>26</i><i>27</i><i>28</i><i>29</i><i>30</i><i></i><i></i>
    </div>
    <div class="cal-nav"><span>&laquo; JAN</span><strong>FEBRUARY</strong><span>MAR &raquo;</span></div>
  </aside>
</div>

<footer class="footer">
  <nav><a>Home</a><span class="sep">|</span><a>About</a><span class="sep">|</span><a>Services</a><span class="sep">|</span><a>Blog</a><span class="sep">|</span><a>Events</a><span class="sep">|</span><a>Testimonials</a><span class="sep">|</span><a>Contact us</a></nav>
  <p>Copyrioght &copy; 2014 Kaljuranna Meeskoor. All rights reserved</p>
</footer>
<div class="social"><span></span><span></span><span></span><span></span></div>
</body>
</html>
```